Store Promo Card (already have logo!)

I need a card design (single side) for my online women’s gift shop containing a promotional code to be placed in bags for attendees at an event. I’m flexible on both shape and sizing, but perhaps a 4x6 card.
—It should contain my attached logo, my website (www.corvidtpq.com), and my Instagram handle (@corvidtpq) and promotion language such as “15% off your purchase with code: MIRVOL”.
—I think I would like my logo to be large.
—It should be clean, simple and modern in design and should use the colors from my logo.
—I would like about 3-5 product pictures depending on design.
Target Market(s)
Women ages 30 to 60
Industry/Entity Type
Retail Upscale Gift
Look and feel

```html
<!DOCTYPE html>
<html lang="en">
<head>
<meta charset="UTF-8">
<title>Corvid TPQ – Promo Card</title>
<link rel="stylesheet" href="https://fonts.googleapis.com/css2?family=Cormorant+Garamond:wght@300;700&family=Josefin+Sans:wght@300;400&display=swap">
<style>
  :root {
    --blush: #efd9d5;
    --charcoal: #333333;
    --slate: #6a6a6a;
    --mist: #ececec;
    --white: #ffffff;
    --rose-line: #f1cfc8;
    --lavender: #b8a6b6;
    --pom: #e9d3cc;
    --gold: #d8ad4c;
  }
  * { margin: 0; padding: 0; box-sizing: border-box; }
  html, body { width: 1200px; height: 763px; overflow: hidden; background: var(--white); }
  .card { position: relative; width: 1200px; height: 763px; background: var(--white); overflow: hidden; }

  .brand-block { position: absolute; left: 0; top: 0; width: 619px; height: 312px; background: var(--blush); }
  .brand-name {
    position: absolute; left: 0; top: 70px; width: 619px; text-align: center;
    font-family: "Cormorant Garamond", Georgia, serif; font-weight: 700;
    color: var(--slate); letter-spacing: 6px; line-height: 1;
  }
  .brand-name .main { display: block; font-size: 112px; }
  .brand-name .sub { display: block; font-size: 30px; letter-spacing: 8px; margin-top: 14px; }

  .product-slippers {
    position: absolute; left: 30px; top: 340px; width: 560px; height: 400px;
    background: radial-gradient(ellipse at 55% 40%, var(--pom) 0%, #dcc6c6 45%, var(--lavender) 75%, var(--white) 100%);
  }

  .social-band { position: absolute; left: 619px; top: 0; width: 101px; height: 763px; background: var(--charcoal); }
  .vertical-text {
    position: absolute; left: 50%; white-space: nowrap; color: var(--white);
    font-family: "Josefin Sans", Arial, sans-serif; font-weight: 300;
    transform: translate(-50%, -50%) rotate(-90deg);
  }
  .handle { top: 162px; font-size: 25px; letter-spacing: 1px; }
  .social-dot { position: absolute; left: 29px; top: 262px; width: 42px; height: 42px; border-radius: 50%; background: var(--blush); }
  .website { top: 540px; font-size: 44px; letter-spacing: 1px; }

  .jewelry-panel { position: absolute; left: 720px; top: 0; width: 480px; height: 312px; background: var(--white); }
  .product-earrings {
    position: absolute; left: 220px; top: 20px; width: 240px; height: 150px; border-radius: 20px;
    background: radial-gradient(ellipse at center, #efd28a 0%, var(--gold) 50%, var(--white) 85%);
  }

  .offer-panel { position: absolute; left: 720px; top: 312px; width: 480px; height: 451px; background: var(--mist); }
  .rose-top {
    position: absolute; left: 10px; top: 8px; width: 160px; height: 150px; border-radius: 50%;
    background: radial-gradient(circle, rgba(241,207,200,0.55) 0%, rgba(241,207,200,0) 70%);
  }
  .rose-bottom {
    position: absolute; left: 370px; top: 320px; width: 110px; height: 131px; border-radius: 50%;
    background: radial-gradient(circle, rgba(241,207,200,0.55) 0%, rgba(241,207,200,0) 70%);
  }
  .offer-box { position: absolute; left: 91px; top: 67px; width: 346px; height: 317px; background: var(--white); }
  .offer-frame { position: absolute; inset: 14px; border: 1.5px solid #d8d8d8; }
  .offer-text { position: absolute; inset: 0; text-align: center; color: var(--charcoal); padding-top: 58px; }
  .offer-amount { font-family: "Cormorant Garamond", Georgia, serif; font-weight: 300; font-size: 112px; line-height: 0.9; }
  .offer-off { font-family: "Josefin Sans", Arial, sans-serif; font-weight: 400; font-size: 30px; letter-spacing: 2px; margin-top: 8px; }
  .offer-detail { font-family: "Josefin Sans", Arial, sans-serif; font-weight: 300; font-size: 22px; margin-top: 2px; }
  .offer-code { font-family: "Josefin Sans", Arial, sans-serif; font-weight: 300; font-size: 28px; letter-spacing: 1px; margin-top: 4px; }
</style>
</head>
<body>
<main class="card">
  <section class="brand-block">
    <h1 class="brand-name"><span class="main">CORVID</span><span class="sub">TPQ</span></h1>
  </section>

  <div class="product-slippers" role="img" aria-label="Photo of lavender velvet slippers with blush pom-poms"></div>

  <aside class="social-band">
    <span class="vertical-text handle">@corvidtpq</span>
    <span class="social-dot"></span>
    <span class="vertical-text website">corvidtpq.com</span>
  </aside>

  <section class="jewelry-panel">
    <div class="product-earrings" role="img" aria-label="Photo of gold clover stud earrings with crystals"></div>
  </section>

  <section class="offer-panel">
    <div class="rose-top" role="img" aria-label="Faint blush rose line drawing"></div>
    <div class="rose-bottom" role="img" aria-label="Faint blush rose line drawing"></div>
    <div class="offer-box">
      <div class="offer-frame"></div>
      <div class="offer-text">
        <p class="offer-amount">15%</p>
        <p class="offer-off">OFF</p>
        <p class="offer-detail">your entire purchase</p>
        <p class="offer-code">code: MIRVOL</p>
      </div>
    </div>
  </section>
</main>
</body>
</html>
```